Navelo Partnering Business Card

Hello everyone. We need a business card design that would match our logo and the theme we're trying to have for Navelo that you can find on our website and/or Corvapage page

```html
<!DOCTYPE html>
<html lang="en">
<head>
<meta charset="utf-8">
<title>Navelo Business Card</title>
<link rel="stylesheet" href="https://fonts.googleapis.com/css2?family=Jost:wght@400;500;600&display=swap">
<style>
  :root {
    --backdrop: #e4e4e4;
    --card-white: #f7f7f7;
    --brand-purple: #2f1f54;
    --accent-grey: #a9a9a9;
    --text-grey: #555555;
    --title-grey: #9a9a9a;
    --divider: #d0d0d0;
    --on-purple: #ffffff;
  }
  * { margin: 0; padding: 0; box-sizing: border-box; }
  html, body {
    width: 1200px; height: 960px; overflow: hidden;
    background: var(--backdrop);
    font-family: "Jost", "Futura", sans-serif;
  }
  .canvas { position: relative; width: 1200px; height: 960px; }

  .card {
    position: absolute; width: 600px; height: 343px; overflow: hidden;
    box-shadow: 0 2px 4px rgba(0,0,0,0.25);
  }
  .card--front { left: 314px; top: 113px; background: var(--card-white); }
  .card--back { left: 311px; top: 472px; background: var(--brand-purple); }

  .wordmark {
    position: absolute; display: flex; align-items: center; gap: 10px;
    font-weight: 600; font-size: 52px; letter-spacing: -0.5px; line-height: 1;
  }
  .wordmark__dot { width: 16px; height: 16px; border-radius: 50%; }
  .card--front .wordmark { left: 82px; top: 138px; color: var(--brand-purple); }
  .card--front .wordmark__dot { background: var(--brand-purple); }
  .card--back .wordmark { left: 0; width: 600px; justify-content: center; top: 140px; color: var(--on-purple); }
  .card--back .wordmark__dot { background: var(--on-purple); }

  .divider {
    position: absolute; left: 316px; top: 84px; width: 1px; height: 178px;
    background: var(--divider);
  }

  .contact { position: absolute; left: 345px; top: 85px; color: var(--text-grey); }
  .contact__name {
    font-size: 21px; font-weight: 500; color: var(--brand-purple);
    line-height: 1; letter-spacing: 0.3px;
  }
  .contact__title {
    font-size: 15px; color: var(--title-grey); line-height: 1; margin-top: 5px;
  }
  .contact__address { font-size: 14.5px; line-height: 18px; margin-top: 13px; }
  .contact__list { list-style: none; margin-top: 10px; font-size: 14.5px; }
  .contact__list li { display: flex; align-items: center; height: 19.5px; }
  .contact__icon { width: 12px; height: 12px; margin-right: 10px; fill: var(--brand-purple); }

  .accent-band { position: absolute; left: 0; bottom: 0; width: 600px; height: 12px; }

  .card__web {
    position: absolute; left: 0; width: 600px; top: 292px; text-align: center;
    color: var(--on-purple); font-size: 15px; letter-spacing: 8px;
    padding-left: 8px;
  }
</style>
</head>
<body>
<main class="canvas">

  <section class="card card--front" aria-label="Card front">
    <div class="wordmark"><span class="wordmark__dot"></span>Navelo</div>
    <div class="divider"></div>
    <div class="contact">
      <p class="contact__name">ELENA MARSH</p>
      <p class="contact__title">CEO/FOUNDER</p>
      <p class="contact__address">4120 Birchwood Lane<br>Juneau, Alaska 34891</p>
      <ul class="contact__list">
        <li>
          <svg class="contact__icon" viewBox="0 0 24 24"><path d="M6.6 10.8a15.1 15.1 0 0 0 6.6 6.6l2.2-2.2c.3-.3.7-.4 1-.2 1.1.4 2.3.6 3.6.6.6 0 1 .4 1 1V20c0 .6-.4 1-1 1A17 17 0 0 1 3 4c0-.6.4-1 1-1h3.5c.6 0 1 .4 1 1 0 1.3.2 2.5.6 3.6.1.3 0 .7-.2 1z"/></svg>
          512 904 3316
        </li>
        <li>
          <svg class="contact__icon" viewBox="0 0 24 24"><path d="M7 1h10a2 2 0 0 1 2 2v18a2 2 0 0 1-2 2H7a2 2 0 0 1-2-2V3a2 2 0 0 1 2-2zm0 3v14h10V4zm5 15.5a1.2 1.2 0 1 0 0 2.4 1.2 1.2 0 0 0 0-2.4z"/></svg>
          744 218 6057
        </li>
        <li>
          <svg class="contact__icon" viewBox="0 0 24 24"><path d="M2 5h20v14H2zm2 2v.5l8 5 8-5V7zm0 2.8V17h16V9.8l-8 5z"/></svg>
          hello@navelo.com
        </li>
        <li>
          <svg class="contact__icon" viewBox="0 0 24 24"><circle cx="12" cy="12" r="10"/><path d="M7 8c2 0 3 1 3 3s-2 2-2 4M14 4c0 2 2 2 2 4s-2 3 0 5 3 1 3 1" stroke="#f7f7f7" stroke-width="1.6" fill="none"/></svg>
          www.navelo.com
        </li>
      </ul>
    </div>
    <svg class="accent-band" viewBox="0 0 600 12" preserveAspectRatio="none" aria-hidden="true">
      <polygon points="0,0 395,0 391,12 0,12" fill="var(--brand-purple)"/>
      <polygon points="397,0 600,0 600,12 393,12" fill="var(--accent-grey)"/>
    </svg>
  </section>

  <section class="card card--back" aria-label="Card back">
    <div class="wordmark"><span class="wordmark__dot"></span>Navelo</div>
    <p class="card__web">www.navelo.com</p>
  </section>

</main>
</body>
</html>
```